Posters to advertise a jewellery design school

I would like two pieces of artwork designing for our jewellery design school in Kuala Lumpur Malaysia.
60cm by 180cm poster
100cm by 100cm poster

My personal style is ‘perfectly imperfect’ but we wold like to show that we give quality classes in a fun and artistic / creative environment

The posters must contain our logo and you can choose to use as many or as few images as you like to tell the story or even include hand drawn line images.

https://files.mistreloom.net/share/folders/7kQpR2xZ9mWt4LbN__yHc8sDe3JfVa6g?usp=sharing

Please include the following wording on the poster
So you want to be a jewellery designer?

Part time and full-time classes available in:
Silversmithing
Jewellery design and rendering
Stone setting
Gemmology
Enamelling
Computer aided design
60cm by 180cm poster
100cm by 100cm poster

The posters must contain our logo and you can choose to use as many or as few images as you like to tell the story.

Silversmithing
Stone setting
Gemmology
Enamelling
Computer aided design

60cm by 180cm poster
100cm by 100cm poster

Silversmithing
Stone setting
Gemmology
Enamelling
Computer aided design

```html
<!DOCTYPE html>
<html lang="en">
<head>
<meta charset="utf-8">
<title>Mara Lindqvist Jewellery – School Poster</title>
<link href="https://fonts.googleapis.com/css2?family=Montserrat:wght@800&family=Nunito:wght@800;900&family=Raleway:wght@400&display=swap" rel="stylesheet">
<style>
  :root{
    --teal:#3b7e84;
    --teal-ring:#46989d;
    --ink:#222222;
    --soft-ink:#333333;
    --pill-grey:#eeeeee;
    --paper:#ffffff;
    --backdrop:#e6e6e6;
    --brand-grey:#4a4a4a;
  }
  html,body{margin:0;padding:0;overflow:hidden;}
  body{width:1165px;height:1200px;background:var(--backdrop);position:relative;}
  .poster{position:absolute;left:0;top:17px;width:1165px;height:1165px;background:var(--paper);overflow:hidden;}
  .artwork{position:absolute;left:0;top:0;}

  .brand{position:absolute;left:66px;top:37px;width:400px;text-align:center;color:var(--brand-grey);font-family:'Raleway',sans-serif;font-weight:400;white-space:nowrap;}
  .brand-dot{width:118px;height:118px;border:2px solid #6a6a6a;border-radius:50%;margin:0 auto 12px;box-sizing:border-box;}
  .brand-name{font-size:33px;letter-spacing:0.5px;line-height:1;}
  .brand-sub{font-size:20px;letter-spacing:2px;margin-top:6px;}

  .intro{position:absolute;left:58px;top:268px;margin:0;font-family:'Raleway',sans-serif;font-size:44px;line-height:1.2;color:var(--ink);font-weight:400;}
  .headline{position:absolute;left:36px;top:334px;margin:0;font-family:'Montserrat',sans-serif;font-weight:800;color:var(--teal);font-size:77px;line-height:77px;letter-spacing:-1px;}

  .class-badge{position:absolute;left:37px;top:522px;width:508px;height:90px;border-radius:45px;background:var(--teal);color:#fff;font-family:'Nunito',sans-serif;font-weight:800;font-size:31px;line-height:36px;text-align:center;display:flex;align-items:center;justify-content:center;}

  .course-list{position:absolute;left:40px;top:624px;margin:0;padding:0;list-style:none;width:538px;font-family:'Nunito',sans-serif;font-weight:900;font-size:34px;}
  .course{height:50px;line-height:50px;padding-left:30px;margin-bottom:7.5px;border-radius:25px;}
  .course--accent{color:var(--teal);}
  .course--shaded{background:var(--pill-grey);color:var(--soft-ink);}

  .contact-band{position:absolute;left:0;top:988px;width:1165px;height:177px;background:var(--teal);color:#fff;font-family:'Montserrat',sans-serif;font-weight:800;text-align:center;}
  .contact-phone{font-size:66px;line-height:72px;margin-top:12px;letter-spacing:-1px;}
  .contact-web{font-size:58px;line-height:70px;letter-spacing:-2px;}
</style>
</head>
<body>
<main class="poster">
  <svg class="artwork" width="1165" height="1165" viewBox="0 0 1165 1165">
    <defs>
      <linearGradient id="studioWall" x1="0" y1="0" x2="0" y2="1">
        <stop offset="0" stop-color="#6f7375"/>
        <stop offset="0.3" stop-color="#8d9193"/>
        <stop offset="0.5" stop-color="#b39a86"/>
        <stop offset="0.7" stop-color="#2e3038"/>
        <stop offset="1" stop-color="#23252d"/>
      </linearGradient>
      <radialGradient id="studioLight" cx="0.45" cy="0.2" r="0.5">
        <stop offset="0" stop-color="#b9c9d6" stop-opacity="0.55"/>
        <stop offset="1" stop-color="#b9c9d6" stop-opacity="0"/>
      </radialGradient>
      <linearGradient id="benchWarm" x1="0" y1="0" x2="1" y2="1">
        <stop offset="0" stop-color="#e5d6c1"/>
        <stop offset="0.5" stop-color="#a8866a"/>
        <stop offset="1" stop-color="#3c3431"/>
      </linearGradient>
      <linearGradient id="benchCool" x1="1" y1="0" x2="0" y2="1">
        <stop offset="0" stop-color="#efe7de"/>
        <stop offset="0.5" stop-color="#b49479"/>
        <stop offset="1" stop-color="#2c2b2e"/>
      </linearGradient>
      <radialGradient id="pieceGold" cx="0.5" cy="0.5" r="0.6">
        <stop offset="0" stop-color="#c9a54a"/>
        <stop offset="0.45" stop-color="#e6d7a8"/>
        <stop offset="1" stop-color="#ffffff"/>
      </radialGradient>
      <radialGradient id="pieceSilver" cx="0.5" cy="0.5" r="0.6">
        <stop offset="0" stop-color="#d6c36a"/>
        <stop offset="0.5" stop-color="#dcdcd6"/>
        <stop offset="1" stop-color="#ffffff"/>
      </radialGradient>
      <radialGradient id="pieceOpal" cx="0.5" cy="0.5" r="0.6">
        <stop offset="0" stop-color="#4f6d7a"/>
        <stop offset="0.5" stop-color="#b7a98a"/>
        <stop offset="1" stop-color="#ffffff"/>
      </radialGradient>
      <radialGradient id="shadowTone">
        <stop offset="0" stop-color="#000" stop-opacity="0.25"/>
        <stop offset="1" stop-color="#000" stop-opacity="0"/>
      </radialGradient>
    </defs>

    <g class="hero-photo" role="img" aria-label="Group of smiling students in aprons standing in the studio beneath a screen showing a stone-setting close-up">
      <circle cx="905" cy="225" r="374" fill="var(--teal)"/>
      <circle cx="905" cy="225" r="361" fill="url(#studioWall)"/>
      <circle cx="905" cy="225" r="361" fill="url(#studioLight)"/>
    </g>

    <g class="workshop-photo" role="img" aria-label="Student in a hat working at a jeweller's bench">
      <circle cx="663" cy="500" r="88" fill="var(--teal-ring)"/>
      <circle cx="663" cy="500" r="79" fill="url(#benchWarm)"/>
    </g>
    <g class="workshop-photo" role="img" aria-label="Student filing a piece at the bench">
      <circle cx="854" cy="576" r="90" fill="var(--teal-ring)"/>
      <circle cx="854" cy="576" r="81" fill="url(#benchCool)"/>
    </g>
    <g class="workshop-photo" role="img" aria-label="Student in safety glasses soldering at the bench">
      <circle cx="1062" cy="558" r="89" fill="var(--teal-ring)"/>
      <circle cx="1062" cy="558" r="80" fill="url(#benchWarm)"/>
    </g>

    <g class="product-photo" role="img" aria-label="Gold ring set with a red centre stone and small gems">
      <ellipse cx="683" cy="920" rx="28" ry="4" fill="url(#shadowTone)"/>
      <circle cx="683" cy="822" r="78" fill="var(--teal)"/>
      <circle cx="683" cy="822" r="70" fill="url(#pieceGold)"/>
    </g>
    <g class="product-photo" role="img" aria-label="Stack of silver and gold rings set with green stones">
      <ellipse cx="868" cy="920" rx="28" ry="4" fill="url(#shadowTone)"/>
      <circle cx="868" cy="822" r="78" fill="var(--teal)"/>
      <circle cx="868" cy="822" r="70" fill="url(#pieceSilver)"/>
    </g>
    <g class="product-photo" role="img" aria-label="Pair of opal drop earrings with dark enamel frames">
      <ellipse cx="1054" cy="920" rx="28" ry="4" fill="url(#shadowTone)"/>
      <circle cx="1054" cy="822" r="78" fill="var(--teal)"/>
      <circle cx="1054" cy="822" r="70" fill="url(#pieceOpal)"/>
    </g>
  </svg>

  <div class="brand">
    <div class="brand-dot"></div>
    <div class="brand-name">MARA LINDQVIST</div>
    <div class="brand-sub">jewellery</div>
  </div>

  <p class="intro">So you want to be a</p>
  <h1 class="headline">JEWELLERY<br>DESIGNER?</h1>

  <div class="class-badge">Part Time And Full-Time<br>Classes Available</div>

  <ul class="course-list">
    <li class="course course--accent">Silversmithing</li>
    <li class="course course--shaded">Jewellery Design &amp; Rendering</li>
    <li class="course course--accent">Stone setting</li>
    <li class="course course--shaded">Gemmology</li>
    <li class="course course--accent">Enamelling</li>
    <li class="course course--shaded">Computer aided design</li>
  </ul>

  <footer class="contact-band">
    <div class="contact-phone">+60 10000 4812</div>
    <div class="contact-web">www.maralindqvistjewellery.com</div>
  </footer>
</main>
</body>
</html>
```